PLV Flyer

We need a professional design for flyers that we produce. The attached event draft is typical of the majority of flyers we will produce, and is the one that we need to do right now.

We would also like the source files for the design. We don’t have Corel Draw, but can work with any files produced in Adobe Creative Suite products.

Target Market(s)

Owners of residential apartments

Industry/Entity Type

Non-Profit

Requirements
Must have
• Design must be complimentary to our new website design at www.plv.org.au so we can establish consistent branding.
• Any fonts used must be freely avalaible standard fonts used in Microsoft Word

```html
<!DOCTYPE html>
<html lang="en">
<head>
<meta charset="utf-8">
<title>PLV Educational Workshop Flyer</title>
<link rel="stylesheet" href="https://fonts.googleapis.com/css2?family=Didact+Gothic&family=Open+Sans:wght@400;600&display=swap">
<style>
  :root {
    --navy: #27306f;
    --orange: #f08a1c;
    --sky-light: #eef4f9;
    --sky-mid: #c9d9e7;
    --sky-deep: #9fb6cc;
    --panel: #dfe5ea;
    --panel-line: #ffffff;
    --white: #ffffff;
  }
  * { margin: 0; padding: 0; box-sizing: border-box; }
  html, body { width: 848px; height: 1200px; overflow: hidden; background: var(--white); }
  .flyer {
    position: relative; width: 848px; height: 1200px; overflow: hidden;
    font-family: "Open Sans", Verdana, sans-serif; color: var(--navy);
    background: var(--white);
  }
  .hero-photo {
    position: absolute; left: 0; top: 0; width: 848px; height: 710px;
    background:
      radial-gradient(ellipse 60% 38% at 50% 76%, #8a7a70 0%, rgba(138,122,112,0.55) 45%, rgba(138,122,112,0) 75%),
      linear-gradient(180deg, var(--sky-light) 0%, #e3ecf4 30%, var(--sky-mid) 55%, var(--sky-deep) 100%);
  }
  .hero-curve { position: absolute; left: 0; top: 540px; width: 848px; height: 200px; }
  .brand {
    position: absolute; left: 54px; top: 30px; display: flex; align-items: flex-start; gap: 10px;
  }
  .brand-mark { width: 54px; height: 62px; background: var(--navy); margin-top: 2px; }
  .brand-name {
    font-family: "Didact Gothic", "Century Gothic", sans-serif; font-size: 22px; line-height: 19px;
    letter-spacing: 1.5px; color: var(--navy); text-transform: uppercase; padding-top: 20px;
  }
  .event-heading {
    position: absolute; left: 0; top: 154px; width: 848px; text-align: center;
    font-family: "Didact Gothic", "Century Gothic", sans-serif; font-weight: 400;
  }
  .event-title { font-size: 31px; line-height: 38px; font-weight: 400; color: var(--orange); }
  .event-subtitle { margin-top: 2px; font-size: 24px; line-height: 32px; font-weight: 400; color: var(--navy); }
  .event-dates { font-size: 24px; line-height: 32px; color: var(--navy); }

  .details { position: absolute; left: 32px; top: 616px; width: 470px; font-size: 12.5px; line-height: 17px; }
  .details .intro, .details .lead { margin-bottom: 8px; }
  .details ul { list-style: none; margin-bottom: 8px; }
  .details li { padding-left: 12px; position: relative; margin-bottom: 7px; }
  .details li:last-child { margin-bottom: 0; }
  .details li::before { content: "\2022"; position: absolute; left: 0; }
  .facts { display: grid; grid-template-columns: 68px 1fr; margin-bottom: 10px; }
  .register { padding-left: 54px; }

  .programme-panel {
    position: absolute; left: 541px; top: 698px; width: 307px; height: 228px;
    background: var(--panel); font-size: 10px; line-height: 15px;
  }
  .programme-panel .timeline { position: absolute; left: 0; top: 0; }
  .programme-panel .cell { position: absolute; }

  .programme { position: absolute; left: 32px; top: 938px; width: 800px; font-size: 12.5px; line-height: 17px; }
  .theme { position: absolute; left: 32px; top: 1058px; width: 806px; font-size: 10.5px; line-height: 15px; }
  .call-to-action {
    position: absolute; left: 0; top: 1171px; width: 848px; text-align: center;
    font-size: 10px; line-height: 14px; letter-spacing: 1.4px; color: var(--orange); text-transform: uppercase;
  }
</style>
</head>
<body>
<div class="flyer">
  <div class="hero-photo" role="img" aria-label="Bright office backdrop with six smiling business people standing in a row in suits"></div>
  <svg class="hero-curve" viewBox="0 0 848 200" aria-hidden="true">
    <path d="M0 58 C 250 40, 420 120, 848 165 L848 200 L0 200 Z" fill="var(--white)"/>
    <g fill="var(--white)">
      <path d="M313 60 l8 0 l9 10 l-9 10 l-8 0 l9 -10 z"/>
      <path d="M334 64 l8 0 l9 10 l-9 10 l-8 0 l9 -10 z"/>
      <path d="M355 69 l8 0 l9 10 l-9 10 l-8 0 l9 -10 z"/>
    </g>
  </svg>

  <div class="brand">
    <span class="brand-mark"></span>
    <span class="brand-name">Property<br>Living<br>Voice</span>
  </div>

  <header class="event-heading">
    <h1 class="event-title">PLV Educational Workshop</h1>
    <h2 class="event-subtitle">“The Essentials of Strata Living – What Every Owner Needs to Know”</h2>
    <p class="event-dates">12th and 26th June 2010</p>
  </header>

  <section class="details">
    <p class="intro">This workshop is for owners in strata<br>apartments who want to learn more about</p>
    <ul>
      <li>getting the best out of apartment living</li>
      <li>protecting their home and their investment</li>
    </ul>
    <p class="lead">AND particularly for</p>
    <ul>
      <li>executive committee members to know their rights and responsibilities in managing their strata scheme</li>
    </ul>
    <div class="facts">
      <span>Location:</span><span>Harbourside Club<br>24 Shoreline Parade<br>Bayview Point 2061</span>
    </div>
    <div class="facts">
      <span>Dates:</span><span>The workshop will run twice – on 12th June and 26th June 2010</span>
      <span>Time:</span><span>10.00 am to 4.00 pm.</span>
      <span>Cost:</span><span>$60.00, which includes morning tea and lunch.</span>
    </div>
    <p>The maximum number of participants for each workshop is 60.</p>
    <p class="register">Register at www.plv.org.au</p>
  </section>

  <aside class="programme-panel">
    <svg class="timeline" width="307" height="228" viewBox="0 0 307 228" aria-hidden="true">
      <path d="M57 228 L57 132 Q57 116 68 106 L68 0" stroke="var(--panel-line)" stroke-width="2" fill="none"/>
      <path d="M62 60 l6 -7 l6 7" stroke="var(--panel-line)" stroke-width="2" fill="none"/>
      <path d="M62 100 l6 -7 l6 7" stroke="var(--panel-line)" stroke-width="2" fill="none"/>
      <path d="M51 180 l6 -7 l6 7" stroke="var(--panel-line)" stroke-width="2" fill="none"/>
    </svg>
    <span class="cell" style="left:72px;top:30px">Topic</span>
    <span class="cell" style="left:133px;top:30px">Speaker</span>
    <span class="cell" style="left:8px;top:46px">Morning</span>
    <span class="cell" style="left:72px;top:46px">Governance</span>
    <span class="cell" style="left:133px;top:46px">Martin Hale,<br>strata lawyer</span>
    <span class="cell" style="left:72px;top:78px">Management</span>
    <span class="cell" style="left:133px;top:78px">Peter Dunmore,<br>seasoned former<br>chairperson and<br>executive<br>committee member</span>
    <span class="cell" style="left:8px;top:160px">Afternoon</span>
    <span class="cell" style="left:72px;top:160px">Financials</span>
    <span class="cell" style="left:133px;top:160px">Alan Whitford,<br>accountant</span>
    <span class="cell" style="left:72px;top:190px">Physicality</span>
    <span class="cell" style="left:133px;top:190px">Tony Ravello,<br>facilities manager</span>
  </aside>

  <section class="programme">
    <p>Programme:<br>The day will comprise four sessions, each facilitated by a specialist. In each session the speaker will provide relevant information and set the topics for group work; participants will break into groups and work up solutions to each topic; and the groups will compare outcomes.</p>
  </section>

  <section class="theme">
    <p>The day’s theme will be:</p>
    <p>Gina is a new owner in her building called Utopia Tower. She notices some management processes which to her seem strange. She is elected to the executive committee and finds that the developer has retained more control than she realised - the service providers have long-term and onerous contracts, and she doesn’t seem to be able to exert enough influence. What does the law require her to do, as a committee member? How does she influence good management processes? The finances seem to be out of control, so how can she fix them so she doesn’t pay inflated levies each year and lose value on her investment? ... and then the neighbour above her apartment installs a timber floor and she has noise problems ... and the building seems to have a lot of defects ............</p>
  </section>

  <p class="call-to-action">Enroll now · Learn a lot · Have some fun as well · Share experiences · Find out how<br>PLV can help you in the longer term.</p>
</div>
</body>
</html>
```